Travesco Business Cards

We need a business card design for Travesco Mining.

This is a B2B company that buys and sells large machinery tires within the coal mining industry. The design should the strong, crisp and masculine. I have uploaded the company logo and rough mock-up of what the back of the card should look like. the front of the card should have the same look/feel as the back. I need editable templates for both the front and the back of the card.

Color scheme should be grey/green/black

Contact information to include on the card:
Name: Dale Pemberton
Title: Managing Director
Phone: 214-503-6192
Address: 1185 Wexley #3 Dallas, TX 75211
Email: Dale@Travesco-example.com

I am also opening a contest for letterhead design. If you submit a business card design, please also submit a letterhead design with the same look/feel. The winner of the business card design will also will the letter head and be paid for both.

Target Market(s)

Procurement men/women in the coal mining industry

Industry/Entity Type

Coal Mining

```html
<!DOCTYPE html>
<html lang="en">
<head>
<meta charset="utf-8">
<title>Travesco Mining Business Cards</title>
<link rel="stylesheet" href="https://fonts.googleapis.com/css2?family=Ubuntu:wght@400;500;700&display=swap">
<style>
  :root {
    --page-bg: #e9e7e4;
    --card-bg: #2b2c2c;
    --card-texture-a: #333434;
    --card-texture-b: #262727;
    --accent-green: #5ab031;
    --text-white: #f2f2f2;
    --text-soft: #d9d9d9;
  }
  * { margin: 0; padding: 0; box-sizing: border-box; }
  html, body { width: 1200px; height: 900px; overflow: hidden; }
  body {
    position: relative;
    background: var(--page-bg);
    font-family: "Ubuntu", sans-serif;
    color: var(--text-white);
  }
  .card {
    position: absolute;
    left: 353px;
    width: 490px;
    height: 280px;
    background: var(--card-bg);
    border-radius: 3px;
    overflow: hidden;
    box-shadow: 0 2px 6px rgba(0,0,0,0.25);
  }
  .card--front { top: 161px; }
  .card--back { top: 471px; }

  .texture {
    position: absolute;
    inset: 0;
  }
  .card--front .texture {
    left: 250px;
    background: linear-gradient(90deg, var(--card-bg), var(--card-texture-a) 60%, var(--card-texture-b));
  }
  .card--back .texture {
    background: radial-gradient(ellipse at 30% 45%, var(--card-texture-a), var(--card-texture-b) 75%);
  }

  .brand {
    position: absolute;
    display: flex;
    align-items: center;
    font-weight: 700;
    letter-spacing: 1px;
    text-transform: uppercase;
    color: var(--text-white);
    white-space: nowrap;
  }
  .brand__mark { background: var(--accent-green); flex: none; }
  .card--front .brand { left: 40px; top: 44px; font-size: 22px; gap: 12px; }
  .card--front .brand__mark { width: 22px; height: 22px; }
  .card--back .brand { left: 70px; top: 112px; font-size: 34px; gap: 16px; }
  .card--back .brand__mark { width: 36px; height: 36px; }

  .tab {
    position: absolute;
    left: 0;
    top: 134px;
    width: 17px;
    height: 40px;
    background: var(--accent-green);
    border-radius: 0 6px 6px 0;
  }
  .holder { position: absolute; left: 40px; top: 136px; }
  .holder__name { font-size: 16px; font-weight: 400; line-height: 20px; }
  .holder__title { font-size: 11px; text-transform: uppercase; color: var(--text-soft); line-height: 14px; }

  .contacts { position: absolute; left: 40px; top: 194px; list-style: none; }
  .contacts li {
    display: flex;
    align-items: center;
    height: 21px;
    font-size: 13.5px;
    letter-spacing: 0.2px;
  }
  .contacts svg { width: 12px; height: 12px; margin-right: 20px; flex: none; }

  .website {
    position: absolute;
    left: 0; right: 0;
    top: 215px;
    text-align: center;
    font-size: 13.5px;
    letter-spacing: 0.6px;
  }
  .bottom-bar {
    position: absolute;
    left: 108px;
    bottom: 0;
    width: 274px;
    height: 16px;
    background: var(--accent-green);
    border-radius: 4px 4px 0 0;
  }
</style>
</head>
<body>
  <section class="card card--front" aria-label="Business card front">
    <div class="texture" role="img" aria-label="Subtle hexagon texture"></div>
    <div class="brand"><span class="brand__mark"></span>Travesco Mining</div>
    <div class="tab"></div>
    <div class="holder">
      <p class="holder__name">Dale Pemberton</p>
      <p class="holder__title">Managing Director</p>
    </div>
    <ul class="contacts">
      <li>
        <svg viewBox="0 0 12 12" aria-hidden="true"><path fill="var(--accent-green)" d="M2.4 1l2 2.3-1 1.2a7 7 0 0 0 4.1 4.1l1.2-1 2.3 2-1 1.4C6.4 11.2.8 5.6 1 1.4z"/></svg>
        214-503-6192
      </li>
      <li>
        <svg viewBox="0 0 12 12" aria-hidden="true"><rect x="1" y="2.5" width="10" height="7.5" rx="1" fill="none" stroke="var(--accent-green)" stroke-width="1.4"/><path d="M1.5 3.2L6 7l4.5-3.8" fill="none" stroke="var(--accent-green)" stroke-width="1.4"/></svg>
        Dale@Travesco-example.com
      </li>
      <li>
        <svg viewBox="0 0 12 12" aria-hidden="true"><path fill="var(--accent-green)" d="M6 .8a4 4 0 0 1 4 4c0 3-4 6.8-4 6.8S2 7.8 2 4.8a4 4 0 0 1 4-4zm0 2.3a1.7 1.7 0 1 0 0 3.4 1.7 1.7 0 0 0 0-3.4z"/></svg>
        1185 Wexley #3 Dallas, TX 75211
      </li>
    </ul>
  </section>

  <section class="card card--back" aria-label="Business card back">
    <div class="texture" role="img" aria-label="Subtle hexagon texture"></div>
    <div class="brand"><span class="brand__mark"></span>Travesco Mining</div>
    <p class="website">www.Travesco-example.com</p>
    <div class="bottom-bar"></div>
  </section>
</body>
</html>
```